High Quality Business card for Property Management Agency - Super Classy and professional design

High Quality Business card design.

We need a business card designed for our Property Management Agency.
We are located on Sydney's Northern Beaches and manage beautiful properties along the beach and harbor.
We need a design that oozes modern, classy and professional.
I would like it to be double sided with contact details and logo on the front and just the logo on the back.

I need a print ready PDF version of the file as well as an editable photoshop (PSD) version of the file.

Logo and information details attached.

Target Market(s)

Property owners/investors, Male and Female Aged 28-65

Industry/Entity Type

Real Estate

Contact Information for Business Card

Tom Carrick
Tel: 0467 239 018
Email: tom@harvestlaneestates.com.au
Website: www.harvestlaneestates.com.au
Address: Level 2, 17 Wattlecourt Rd, Dunmarra NSW 2187

Font styles to use
Sans Serif

Requirements
Must have
• - Logo front and back
• - Business card details listed above and attached
• - Colour
Nice to have
• Sleek and professional

```html
<!DOCTYPE html>
<html lang="en">
<head>
<meta charset="utf-8">
<title>Harvest Lane Estates — Business Card</title>
<link href="https://fonts.googleapis.com/css2?family=Arimo:wght@400;700&display=swap" rel="stylesheet">
<style>
  :root {
    --stage: #2b2b2b;
    --card-dark: #141818;
    --card-light: #f4f4f4;
    --ink: #1c1c1c;
    --ink-soft: #333;
    --teal: #1f8f96;
    --logo-light: #e6e6e6;
  }
  * { margin: 0; padding: 0; box-sizing: border-box; }
  html, body { width: 1200px; height: 997px; overflow: hidden; }
  body {
    background: var(--stage);
    font-family: "Arimo", Arial, sans-serif;
    position: relative;
  }
  .card {
    position: absolute;
    left: 290px;
    width: 620px;
    height: 378px;
    border-radius: 22px;
    box-shadow: 0 12px 30px rgba(0,0,0,.45);
    overflow: hidden;
  }
  .card--back { top: 90px; background: var(--card-dark); }
  .card--front { top: 530px; background: var(--card-light); }

  .brand {
    position: absolute;
    display: flex;
    align-items: center;
    gap: 14px;
    font-weight: 700;
    text-transform: uppercase;
    white-space: nowrap;
  }
  .brand__mark { background: var(--teal); flex: none; }
  .card--back .brand {
    left: 0; right: 0; top: 0; bottom: 0;
    justify-content: center;
    color: var(--logo-light);
    font-size: 40px;
  }
  .card--back .brand__mark { width: 26px; height: 26px; }
  .card--front .brand {
    left: 30px; top: 152px;
    color: var(--ink);
    font-size: 20px;
    gap: 9px;
  }
  .card--front .brand__mark { width: 14px; height: 14px; }

  .divider {
    position: absolute;
    left: 336px; top: 70px;
    width: 2px; height: 150px;
    background: linear-gradient(to bottom, rgba(31,143,150,0), var(--teal) 40%, rgba(31,143,150,0));
  }
  .contacts {
    position: absolute;
    left: 362px; top: 92px;
    list-style: none;
    font-size: 13px;
    color: var(--ink-soft);
    line-height: 1.3;
  }
  .contacts li { display: flex; gap: 10px; margin-bottom: 14px; align-items: flex-start; white-space: nowrap; }
  .contacts svg { width: 13px; height: 13px; flex: none; margin-top: 2px; fill: var(--teal); }
  .website {
    position: absolute;
    left: 0; right: 0; bottom: 44px;
    text-align: center;
    font-weight: 700;
    font-size: 18px;
    letter-spacing: .06em;
    color: var(--ink);
  }
</style>
</head>
<body>
  <section class="card card--back" aria-label="Card back">
    <div class="brand"><span class="brand__mark"></span>Harvest Lane Estates</div>
  </section>

  <section class="card card--front" aria-label="Card front">
    <div class="brand"><span class="brand__mark"></span>Harvest Lane Estates</div>
    <div class="divider"></div>
    <ul class="contacts">
      <li>
        <svg viewBox="0 0 16 16" aria-hidden="true"><path d="M2 6c0-2 2-3 6-3s6 1 6 3v1h-3V5.5H5V7H2zM4 8h8l2 5H2z"/></svg>
        <span>0467 239 018</span>
      </li>
      <li>
        <svg viewBox="0 0 16 16" aria-hidden="true"><path d="M1 3h14v10H1zM2.5 4.5 8 9l5.5-4.5v1.3L8 10.3 2.5 5.8z" fill-rule="evenodd"/></svg>
        <span>tom@harvestlaneestates.com.au</span>
      </li>
      <li>
        <svg viewBox="0 0 16 16" aria-hidden="true"><path d="M8 1 1 8h2v7h4v-4h2v4h4V8h2z"/></svg>
        <span>Level 2, 17 Wattlecourt Rd,<br>Dunmarra NSW 2187</span>
      </li>
    </ul>
    <div class="website">www.harvestlaneestates.com.au</div>
  </section>
</body>
</html>
```